Norvane Builders Business Card

Modern and Professional Business Card for a Med size construction/development company.

See the samples below for the design I like … but I need ideas for incorporating the red company logo while still keeping the clean look of the card samples that are attached.

Logo and tag line on the back … info on the front.

Tagline: Solid Work Built from the Footing Up

Target Market(s)

Med-Large General Contractors

Contact Information for Business Card

Norvane Builders Limited
42 Brenton Street
Elk Harbour, NL
B3K 7T2

t: 709-555-0147
f: 709-555-0192
w: www.norvanebuilders-example.com

Font styles to use
Sans Serif

Colors
fbee3e

Requirements
Must have
• I like the black and yellow designs of the attached samples …. but I'm not sure how to incorporate the red Norvane Builders logo into that design??
Nice to have
• Construction safety strips

```html
<!DOCTYPE html>
<html lang="en">
<head>
<meta charset="utf-8">
<title>Norvane Builders Business Card</title>
<link href="https://fonts.googleapis.com/css2?family=Arvo&display=swap" rel="stylesheet">
<style>
  :root {
    --yellow: #f8ec3e;
    --black: #0c0c0c;
    --red: #e5232b;
    --white: #ffffff;
    --page: #f1f1f1;
  }
  * { margin: 0; padding: 0; box-sizing: border-box; }
  html, body { width: 1200px; height: 923px; overflow: hidden; }
  body {
    background: var(--page);
    font-family: "Arvo", Georgia, serif;
    position: relative;
  }
  .card {
    position: absolute;
    left: 290px;
    width: 621px;
    height: 354px;
    overflow: hidden;
    box-shadow: 0 6px 18px rgba(0,0,0,0.18);
  }
  .card--back { top: 83px; background: var(--yellow); }
  .card--front { top: 485px; background: var(--black); }

  .brand-name {
    color: var(--red);
    font-family: "Arvo", Georgia, serif;
    font-weight: 400;
    text-transform: uppercase;
    text-align: center;
    line-height: 1.05;
  }
  .card--back .brand-name {
    position: absolute;
    left: 0; right: 0;
    top: 132px;
    font-size: 40px;
    letter-spacing: 1px;
  }
  .card--back .brand-name small {
    display: block;
    font-size: 20px;
    letter-spacing: 2px;
    margin-top: 6px;
  }
  .tagline-band {
    position: absolute;
    left: 0; right: 0;
    top: 303px;
    height: 29px;
    background: var(--black);
    color: var(--yellow);
    font-size: 16px;
    text-transform: uppercase;
    text-align: center;
    line-height: 29px;
  }

  .card--front .brand-name {
    position: absolute;
    right: 34px;
    top: 32px;
    font-size: 30px;
    text-align: right;
  }
  .card--front .brand-name small {
    display: block;
    font-size: 15px;
    letter-spacing: 1.5px;
    margin-top: 4px;
  }
  .contact {
    position: absolute;
    left: 40px;
    top: 128px;
    color: var(--white);
    font-size: 17px;
    line-height: 26px;
  }
  .contact .company { color: var(--yellow); }
  .contact .lines { margin-top: 12px; }
  .contact .line { display: flex; align-items: center; gap: 10px; height: 26px; }
  .contact svg { width: 22px; height: 18px; }
  .wave { position: absolute; left: 0; top: 0; }
  .website {
    position: absolute;
    right: 34px;
    top: 311px;
    color: var(--black);
    font-size: 16px;
  }
</style>
</head>
<body>
  <section class="card card--back">
    <div class="brand-name">Norvane Builders<small>Limited</small></div>
    <div class="tagline-band">Solid Work Built from the Footing Up</div>
  </section>

  <section class="card card--front">
    <svg class="wave" width="621" height="354" viewBox="0 0 621 354" aria-hidden="true">
      <path d="M0,303 C60,325 110,332 170,330 C240,328 280,300 360,288 C450,276 550,288 621,306 L621,354 L0,354 Z" fill="var(--yellow)"/>
      <path d="M0,268 C70,300 160,318 297,296 C200,324 80,318 0,291 Z" fill="var(--red)"/>
    </svg>

    <div class="brand-name">Norvane Builders<small>Limited</small></div>

    <div class="contact">
      <div class="company">Norvane Builders Limited</div>
      <div>42 Brenton Street</div>
      <div>Elk Harbour, NL, B3K 7T2</div>
      <div class="lines">
        <div class="line">
          <svg viewBox="0 0 22 18" aria-label="Phone"><path d="M2,7 C2,2 20,2 20,7 L16,8 L15,5 C12,4 10,4 7,5 L6,8 Z" fill="var(--yellow)"/><path d="M5,9 L17,9 L19,16 L3,16 Z" fill="var(--yellow)"/><circle cx="11" cy="12.5" r="2" fill="var(--black)"/></svg>
          <span>709 - 555 - 0147</span>
        </div>
        <div class="line">
          <svg viewBox="0 0 22 18" aria-label="Fax"><rect x="1" y="4" width="5" height="13" fill="var(--yellow)"/><rect x="7" y="7" width="14" height="10" fill="var(--yellow)"/><rect x="9" y="1" width="9" height="5" fill="var(--yellow)"/><rect x="10" y="9" width="2" height="2" fill="var(--black)"/><rect x="14" y="9" width="2" height="2" fill="var(--black)"/><rect x="10" y="13" width="2" height="2" fill="var(--black)"/><rect x="14" y="13" width="2" height="2" fill="var(--black)"/></svg>
          <span>709 - 555 - 0192</span>
        </div>
      </div>
    </div>

    <div class="website">www.norvanebuilders-example.com</div>
  </section>
</body>
</html>
```